Brochure Cover Design Project

Need a design for our company brochure cover.
We are a mechanical consulting engineering firm ( HVAC, pLUMBING). We have the brochure

Target Market(s)

Architects and Building Owners

Industry/Entity Type

Hvac

```html
<!DOCTYPE html>
<html lang="en">
<head>
<meta charset="utf-8">
<title>Kinetic Design Studio – Brochure Cover</title>
<link rel="stylesheet" href="https://fonts.googleapis.com/css2?family=Roboto+Condensed:ital,wght@0,700;1,700&display=swap">
<style>
  :root {
    --green-dark: #2e5629;
    --green-mid: #4e8a3f;
    --green-light: #b2d68a;
    --green-text-light: #a9d48a;
    --paper: #ffffff;
  }
  * { margin: 0; padding: 0; box-sizing: border-box; }
  html, body { width: 1200px; height: 869px; overflow: hidden; background: #ffffff; }
  .spread {
    position: relative;
    width: 1200px;
    height: 869px;
    font-family: "Roboto Condensed", "Arial Narrow", sans-serif;
  }
  .back-cover {
    position: absolute; left: 0; top: 0;
    width: 600px; height: 869px;
    background: var(--green-dark);
  }
  .back-cover__contact {
    position: absolute; left: 48px; top: 790px;
    color: var(--green-text-light);
    font-style: italic; font-weight: 700;
    font-size: 17px; line-height: 25px;
  }
  .front-cover {
    position: absolute; left: 600px; top: 0;
    width: 600px; height: 869px;
    background: var(--paper);
  }
  .brand {
    position: absolute; left: 0; top: 176px; width: 600px;
    display: flex; justify-content: center; align-items: center; gap: 14px;
  }
  .brand__mark {
    width: 30px; height: 30px; background: var(--green-mid);
  }
  .brand__name {
    color: var(--green-mid);
    font-weight: 700; font-size: 48px; letter-spacing: 1px;
    line-height: 1;
  }
  .tagline-band {
    position: absolute; left: 0; top: 389px;
    width: 600px; height: 165px;
    background: var(--green-light);
    display: flex; align-items: center; justify-content: center;
  }
  .tagline {
    color: var(--green-dark);
    font-style: italic; font-weight: 700;
    font-size: 45px; line-height: 54px;
    text-align: center; letter-spacing: 0.3px;
  }
  .footer-strip {
    position: absolute; left: 600px; top: 833px;
    width: 600px; height: 36px;
  }
  .footer-strip svg { display: block; }
  .web-address {
    position: absolute; left: 600px; top: 833px;
    width: 598px; height: 36px;
    display: flex; align-items: center; justify-content: center;
    color: #ffffff; font-weight: 700; font-size: 17px; letter-spacing: 4px;
  }
</style>
</head>
<body>
<main class="spread">
  <section class="back-cover">
    <address class="back-cover__contact">
      2240 Alder Ridge Rd. Ste. 210, Cedar Grove, CA 94012<br>
      P: 555-310-0100 x 106, F: 555-310-0144
    </address>
  </section>

  <section class="front-cover">
    <div class="brand">
      <span class="brand__mark"></span>
      <span class="brand__name">KINETIC DESIGN STUDIO</span>
    </div>
    <div class="tagline-band">
      <h1 class="tagline">ENGINEERING THE ART<br>OF THE POSSIBLE</h1>
    </div>
  </section>

  <div class="footer-strip">
    <svg width="600" height="36" viewBox="0 0 600 36">
      <polygon points="0,0 487,0 476,36 0,36" fill="var(--green-dark)"/>
      <polygon points="500,0 600,0 600,36 489,36" fill="var(--green-light)"/>
    </svg>
  </div>
  <div class="web-address">www.kds-eng.com</div>
</main>
</body>
</html>
```